Flyer Design For Building & Decorating Company

We need an A6 double-sided colour flyer for a letter-box marketing campaign. We are a building and decorating company based in West London. We saw a flyer that we liked and have attached it as an example of the sort of thing we're looking for (see attached files Example A6 Flyer - Front.png and Example A6 Flyer - Back.png). Please note that we're not expecting the designer to slavishly follow this design, more to use it as a jumping-off point.

The design must incorporate a strong call to action, e.g., Call Us For A Free, No-Obligation Quote.

The textual information that must be included in the flyer (contact methods, tagline, services, etc.) are included in the attached file Flyer Text.docx.

Also included as attachments are a selection of images used on our website (files bathroom.png, carpentry.png, decorating.jpg,
flooring.jpg, painting_decorating.jpg, repointing.jpg and work_ on_scaffold.jpg). Please include these images on the flyer (at least one image on each side), or use stock images if any of these are unsuitable.

The company logo will also need to be included in the flyer - see attached file logo.png

The images on our website have all had to be re-sized from the originals. I've attached a number of the original images to this brief, as these are the highest resolution versions of the images that we have. I would ask that you use the versions attached to the brief, but if you feel that other images from our website would work better on your flyer design, please let me know and I'll attach them to this brief.

Finally, we've attached guideline notes from our printer (see attached file Printer's Requirements.docx) - please ensure these are adhered to where relevant.

Target Market(s)

People in West London who require building or decorating work to be done on their properties.

Industry/Entity Type

Marketing

Requirements
Must have
• A6 double-sided colour flyer using the text we provided and some of the images provided.

The call to action must be prominent and eye-catching, as the only purpose of the flyer is to get recipients to contact our company for a quote.

```html
<!DOCTYPE html>
<html lang="en">
<head>
<meta charset="utf-8">
<title>K &amp; M Renovations – A6 Flyer Front and Back</title>
<link rel="stylesheet" href="https://fonts.googleapis.com/css2?family=Arimo:ital,wght@0,400;0,700;1,700&display=swap">
<style>
:root{
  --brown-light:#7d4c22;
  --brown-dark:#4f2c12;
  --yellow:#ffe600;
  --ink:#111111;
  --red:#d8192a;
  --navy:#232f6b;
  --white:#ffffff;
  --cream:#f3e2c2;
}
*{margin:0;padding:0;box-sizing:border-box}
html,body{width:1200px;height:763px;overflow:hidden;background:var(--white)}
body{position:relative;font-family:"Arimo",Arial,sans-serif;color:var(--white)}

.flyer{position:absolute;top:2px;width:562px;height:759px;overflow:hidden;
  background:radial-gradient(ellipse at 40% 35%,var(--brown-light) 0%,var(--brown-dark) 100%)}
.flyer--front{left:8px}
.flyer--back{left:602px}

.bands{position:absolute;inset:0;width:562px;height:759px}

.headline{position:absolute;top:12px;left:0;width:100%;text-align:center;
  font-weight:700;font-size:25px;color:var(--yellow);
  -webkit-text-stroke:1.2px var(--ink);paint-order:stroke fill}
.tagline{position:absolute;top:52px;left:0;width:100%;text-align:center;
  font-weight:700;font-size:17px;color:var(--yellow)}

.brand{position:absolute;left:16px;top:88px;display:flex;align-items:center;gap:7px;
  font-weight:700;font-size:15px;color:var(--cream)}
.brand__mark{width:16px;height:16px;background:var(--cream)}

.photo{position:absolute;border:2px solid var(--white)}
.photo--scaffold{left:378px;top:84px;width:184px;height:196px;background:linear-gradient(160deg,#c9d6e2,#8a7a68)}
.photo--house{left:250px;top:178px;width:200px;height:188px;background:linear-gradient(180deg,#b9c7d4,#8c4a33 55%,#6b5a4a)}
.photo--worker{left:158px;top:262px;width:196px;height:178px;background:linear-gradient(150deg,#e8e0d2,#5e6f8a 60%,#8b6c4b)}
.photo--wood{left:0;top:430px;width:204px;height:145px;background:linear-gradient(135deg,#e0b070,#a8702f)}
.photo--before{left:126px;top:86px;width:144px;height:106px;background:linear-gradient(160deg,#e3dccd,#a89b84)}
.photo--after{left:333px;top:86px;width:149px;height:106px;background:linear-gradient(160deg,#f2ead8,#b59a72)}
.photo__tag{position:absolute;left:6px;top:6px;background:var(--red);color:var(--white);
  font-size:10px;font-weight:700;padding:1px 5px;transform:rotate(-20deg)}

.services{position:absolute;left:18px;top:168px}
.services__title{font-size:27px;font-weight:400;margin-bottom:4px}
.services__list{list-style:none;font-size:17px;line-height:21px}

.band-line{position:absolute;transform-origin:0 0;white-space:nowrap;font-weight:700}
.flyer--front .band-line{transform:rotate(-33deg)}
.flyer--back .band-line{transform:rotate(-42deg)}
.band-line--offer{color:var(--yellow);font-size:22px}
.band-line--tel{color:var(--white);font-size:42px;-webkit-text-stroke:1px var(--ink);paint-order:stroke fill}
.band-line--call{color:var(--yellow);font-size:40px;line-height:0.95;
  -webkit-text-stroke:1.5px var(--ink);paint-order:stroke fill}
.flyer--back .band-line--tel{font-size:37px}

.address{position:absolute;text-align:center;line-height:1.3}
.address__title{font-size:22px}
.address__line{font-size:15px}
.address__email{font-size:13px;margin-top:4px}
.address__web{font-size:16px;margin-top:8px}
.flyer--front .address{left:345px;top:598px;width:210px}
.flyer--back .address{left:318px;top:600px;width:240px}

.menu{position:absolute;font-size:12.5px;line-height:18px}
.menu__title{font-size:13.5px;margin-bottom:2px}
.menu ul{list-style:none;margin-bottom:6px}
.menu li::before{content:"• "}
.menu--left{left:12px;top:196px}
.menu--right{left:300px;top:196px}
</style>
</head>
<body>

<section class="flyer flyer--front">
  <svg class="bands" viewBox="0 0 562 759" aria-hidden="true">
    <polygon points="0,590 562,225 562,451 0,816" fill="var(--white)"/>
    <polygon points="0,600 562,235 562,435 0,800" fill="var(--red)"/>
    <polygon points="562,451 562,759 0,759 0,816" fill="var(--navy)"/>
  </svg>

  <div class="photo photo--scaffold" role="img" aria-label="Photo of a brick house front wrapped in scaffolding"></div>
  <div class="photo photo--house" role="img" aria-label="Photo of a red-brick London terraced house"></div>
  <div class="photo photo--worker" role="img" aria-label="Photo of a tradesman fitting a cabinet"></div>
  <div class="photo photo--wood" role="img" aria-label="Photo of timber being cut with a hand saw"></div>

  <h1 class="headline">West London Builders &amp; Decorators</h1>
  <p class="tagline">Quality Renovations at Affordable Prices</p>
  <div class="brand"><span class="brand__mark"></span>K &amp; M Renovations</div>

  <div class="services">
    <h2 class="services__title">Services:</h2>
    <ul class="services__list">
      <li>Bathrooms/Kitchens</li>
      <li>Painting/Decorating</li>
      <li>Electrical Works</li>
      <li>General Repairs</li>
      <li>Tiling</li>
      <li>Plastering</li>
      <li>Carpentry</li>
      <li>Flooring</li>
      <li>Plumbing</li>
      <li>Brickwork</li>
    </ul>
  </div>

  <div class="band-line band-line--call" style="left:14px;top:628px">CALL<br>NOW</div>
  <div class="band-line band-line--offer" style="left:150px;top:530px">For a Free Quote References Available</div>
  <div class="band-line band-line--tel" style="left:125px;top:590px">Tel: 0208 555 0142</div>
  <div class="band-line band-line--tel" style="left:160px;top:640px">Mobile: 07700 900314</div>

  <address class="address" style="font-style:normal">
    <div class="address__title">Address:</div>
    <div class="address__line">K &amp; M Renovations,</div>
    <div class="address__line">14 Larch Grove,</div>
    <div class="address__line">Ealing, London W5 9QT</div>
    <div class="address__email">hello@km-renovations.co.uk</div>
    <div class="address__web">www.km-renovations.co.uk</div>
  </address>
</section>

<section class="flyer flyer--back">
  <svg class="bands" viewBox="0 0 562 759" aria-hidden="true">
    <polygon points="0,766 562,260 562,430 0,936" fill="var(--white)"/>
    <polygon points="0,776 562,270 562,420 0,926" fill="var(--red)"/>
    <polygon points="562,430 562,759 196,759" fill="var(--navy)"/>
  </svg>

  <h1 class="headline">West London Builders &amp; Decorators</h1>
  <p class="tagline">Quality Renovations at Affordable Prices</p>
  <div class="brand"><span class="brand__mark"></span>K &amp; M</div>

  <div class="photo photo--before" role="img" aria-label="Photo of a bare room before renovation"><span class="photo__tag">Before</span></div>
  <div class="photo photo--after" role="img" aria-label="Photo of the finished renovated room"><span class="photo__tag">After</span></div>

  <div class="menu menu--left">
    <h3 class="menu__title">Bathroom/Kitchen:</h3>
    <ul>
      <li>Complete/Partial Fixings</li>
      <li>Tiling</li>
      <li>Sink/Bath/Radiator</li>
      <li>Tap Repairs/Replace</li>
      <li>Fit Washing Machine/Dishwasher</li>
    </ul>
    <h3 class="menu__title">Maintenance/Repairs:</h3>
    <ul>
      <li>Reseal Bath/Shower</li>
      <li>Fit Shelves</li>
      <li>Electrics - Complete/Partial</li>
      <li>Sash/Gutter/Roof Repairs</li>
      <li>Lots more ...</li>
    </ul>
    <h3 class="menu__title">Landscaping/Roof/Work On High Ladders:</h3>
    <ul>
      <li>Fencing/Paving/Decking</li>
      <li>Work On High Ladders/Scaffold</li>
      <li>Tree Cutting/Removal</li>
      <li>Roofing - New/Repair</li>
    </ul>
    <h3 class="menu__title">Decorating:</h3>
    <ul>
      <li>Complete/Partial Works</li>
      <li>Lining/Wallpaper</li>
      <li>Painting Inside/Outside</li>
      <li>Rectify Damage/</li>
      <li>Plastering</li>
    </ul>
  </div>

  <div class="menu menu--right">
    <h3 class="menu__title">Carpentry:</h3>
    <ul>
      <li>Wardrobes/Cupboards</li>
      <li>Shelving/Skirting</li>
      <li>Doors/Windows</li>
      <li>Kitchen/Bathroom Suites</li>
      <li>Wooden Floor/Laminate</li>
    </ul>
  </div>

  <div class="band-line band-line--tel" style="left:118px;top:712px">Tel: 0208 555 0142</div>
  <div class="band-line band-line--tel" style="left:160px;top:738px">Mobile: 07700 900314</div>

  <address class="address" style="font-style:normal">
    <div class="address__title">Address:</div>
    <div class="address__line">K &amp; M Renovations,</div>
    <div class="address__line">14 Larch Grove,</div>
    <div class="address__line">Ealing, London W5 9QT</div>
    <div class="address__email">hello@km-renovations.co.uk</div>
    <div class="address__web">www.km-renovations.co.uk</div>
  </address>
</section>

</body>
</html>
```